Business Card Design

I want to pull elements/colors from Website. Attached is a screen shot. Do not want any buildings/building graphics/construction clichés. This is for a construction management firm but I want to keep it broad enough that I can expand into other areas. I do not want the logo to be limited. Thank you.
Updates

Please review the screen shot of the website. Please use the font and color of Brackwell Holdings, LLC on the website. Please use the tag line "Construction Management in the Palm Beaches" Please show contractor license ... CGC 7390462 You may use the back for the contact information. Please no phone/house icons. It does not have to be a black card. Thank you.

Target Market(s)

Professional people with money. Owners, Architects, Engineers, Developers, Real Estate Agents etc.

Industry/Entity Type

Construction

Contact Information for Business Card

Brackwell Holdings, LLC
Construction Management

Dean T Brackwell
418 Ostrander Court #73
North Palm Beach, FL 33412
(561) 555-0187
www.BrackwellHoldings.example

Requirements
Must have
• Clean, crisp, modern.

Broad enough that it is not trapped into a particular industry.

My goal is to expand into different markets, different industries.

Should not have
• The back of the card should not be colored in any way. Rubs off on other cards.

Do not want any buildings/building graphics/construction clichés.

```html
<!DOCTYPE html>
<html lang="en">
<head>
<meta charset="utf-8">
<title>Brackwell Holdings, LLC — Business Card</title>
<link rel="stylesheet" href="https://fonts.googleapis.com/css2?family=Archivo:ital,wght@1,800&family=Didact+Gothic&display=swap">
<style>
  :root {
    --stage: #d9d6d2;
    --card-black: #050505;
    --card-sheen: #2a2a2c;
    --swoosh-blue: #3d43b0;
    --swoosh-light: #6d74d8;
    --white: #ffffff;
    --grey: #b9b9b9;
    --icon-grey: #d8d8d8;
    --name-blue: #9fd0f0;
  }
  html, body {
    margin: 0;
    padding: 0;
    width: 1200px;
    height: 1200px;
    overflow: hidden;
    background: var(--stage);
  }
  .business-card {
    position: absolute;
    left: 75px;
    top: 300px;
    width: 1050px;
    height: 600px;
    background: radial-gradient(ellipse at 72% 45%, var(--card-sheen) 0%, var(--card-black) 55%);
    overflow: hidden;
    box-shadow: 0 20px 50px rgba(0,0,0,0.35);
    font-family: "Didact Gothic", "Century Gothic", sans-serif;
    color: var(--white);
  }
  .swoosh {
    position: absolute;
    inset: 0;
    width: 100%;
    height: 100%;
  }
  .company-heading {
    position: absolute;
    left: 55px;
    top: 62px;
  }
  .company-name {
    margin: 0;
    font-family: "Archivo", "Arial Black", sans-serif;
    font-weight: 800;
    font-style: italic;
    font-size: 38px;
    letter-spacing: 0.5px;
    color: var(--white);
  }
  .company-tagline {
    margin: 6px 0 0 30px;
    font-size: 19px;
    letter-spacing: 1.2px;
    color: var(--grey);
  }
  .brand-mark {
    position: absolute;
    right: 55px;
    top: 48px;
    width: 250px;
  }
  .brand-square {
    width: 46px;
    height: 46px;
    background: var(--name-blue);
    margin-bottom: 14px;
  }
  .brand-name {
    font-size: 30px;
    line-height: 1.1;
    color: var(--white);
    margin: 0;
  }
  .brand-rule {
    height: 2px;
    background: var(--grey);
    margin: 8px 0 6px;
  }
  .brand-sub {
    font-size: 14px;
    letter-spacing: 1px;
    color: var(--white);
    margin: 0;
  }
  .contact {
    position: absolute;
    left: 48px;
    top: 300px;
  }
  .person-name {
    margin: 0 0 12px 10px;
    font-size: 34px;
    font-weight: 400;
    color: var(--name-blue);
  }
  .contact-line {
    display: flex;
    align-items: center;
    gap: 10px;
    margin: 0 0 9px;
    font-size: 26px;
    line-height: 34px;
    color: var(--white);
    white-space: nowrap;
  }
  .contact-icon,
  .icon-slot {
    width: 26px;
    height: 26px;
    flex: none;
  }
</style>
</head>
<body>
  <article class="business-card">
    <svg class="swoosh" viewBox="0 0 1050 600" aria-hidden="true">
      <defs>
        <linearGradient id="swooshFill" x1="0" y1="0" x2="1" y2="1">
          <stop offset="0" stop-color="var(--swoosh-blue)"/>
          <stop offset="0.6" stop-color="var(--swoosh-blue)"/>
          <stop offset="1" stop-color="var(--swoosh-light)"/>
        </linearGradient>
      </defs>
      <path d="M0,190 C140,205 300,238 520,246 C730,254 900,380 1050,560 L1050,600 C895,410 725,276 520,272 C300,268 140,240 0,228 Z" fill="url(#swooshFill)"/>
    </svg>

    <header class="company-heading">
      <h1 class="company-name">BRACKWELL HOLDINGS, LLC</h1>
      <p class="company-tagline">CONSTRUCTION MANAGEMENT IN THE PALM BEACHES</p>
    </header>

    <div class="brand-mark">
      <div class="brand-square"></div>
      <p class="brand-name">BRACKWELL HOLDINGS, LLC</p>
      <div class="brand-rule"></div>
      <p class="brand-sub">CONSTRUCTION MANAGEMENT</p>
    </div>

    <section class="contact">
      <h2 class="person-name">Dean T Brackwell</h2>
      <p class="contact-line">
        <span class="icon-slot"></span>
        418 Ostrander Court #73 North Palm Beach, FL 33412
      </p>
      <p class="contact-line">
        <span class="icon-slot"></span>
        (561) 555-0187
      </p>
      <p class="contact-line">
        <svg class="contact-icon" viewBox="0 0 24 24" aria-hidden="true"><rect x="2" y="5" width="20" height="14" fill="var(--icon-grey)"/><path d="M2 5 L12 13 L22 5" fill="none" stroke="var(--card-black)" stroke-width="1.6"/></svg>
        brackwellholdings@mail.example
      </p>
      <p class="contact-line">
        <svg class="contact-icon" viewBox="0 0 24 24" aria-hidden="true"><circle cx="12" cy="12" r="9.5" fill="none" stroke="var(--icon-grey)" stroke-width="2"/><ellipse cx="12" cy="12" rx="4" ry="9.5" fill="none" stroke="var(--icon-grey)" stroke-width="1.6"/><path d="M2.5 12 H21.5 M4 7 H20 M4 17 H20" stroke="var(--icon-grey)" stroke-width="1.4"/></svg>
        www.BrackwellHoldings.example
      </p>
      <p class="contact-line">
        <span class="icon-slot"></span>
        CGC 7390462
      </p>
    </section>
  </article>
</body>
</html>
```